Design a two sided Flyer for Each Porch bulk delivery from NPDS - size 8,5" x 11"

We need a flyer that will be accepted by NPDS for each porch bulk delivery (size 8,5" x 11"). It needs to be double sided designed and we have already made the copy writing. We just need a designer to make it look stunning and chique. When our potential customers receive the flyer they should have a feeling that they can improve their house with the right kind of modern lighting. The flyer should be saying in the front cozy, safety, warmth, in short everything you need at home for the winter. (and they can off course buy that at our web store). Having (happy) people on the flyer a bonus. And in the back it will give a couple tips and tricks on how you should light up your home.

We have included in attachment
- a word document with the writing that needs to go on the flyer (front and back)
- our logo in several files and formats

Under are links to our filecrate where you can find many pictures of the lamps we sell but feel free to find others.
- https://www.filecrate.example/sh/qk7tn2r4pz8wvmd/h3LpQrT6Yb
- https://www.filecrate.example/sh/91bvk6sj2pf8rna/mHT5x2K7Nc
- https://www.filecrate.example/sh/pwtt4ajdm38gy6q/_82kFdR4Wq
- https://www.filecrate.example/sh/vnc38sdqe40717h/_pzRtMjwe7

Last but not least our own site:
- http://www.brenovaka.example

Target Market(s)

USA Families in the age of 25-45y old. Medium to high income and open minded

Industry/Entity Type

House

Requirements
Must have
• - minimum of 350 dpi (dot per inch) resolution.
- size 8.5" x 11"
- two sided
- should grab the attention of the reader and give a sense of class, cozy and warmth
Should not have
• no cheap looking, screaming words, flyer

```html
<!DOCTYPE html>
<html lang="en">
<head>
<meta charset="utf-8">
<title>Your guide to the perfect interior lighting</title>
<link href="https://fonts.googleapis.com/css2?family=Open+Sans:ital,wght@0,400;0,600;0,700;1,600;1,700&family=Tinos:wght@400&display=swap" rel="stylesheet">
<style>
  :root {
    --paper-light: #fdfdfd;
    --paper-mid: #efefef;
    --paper-dark: #d2d2d2;
    --ink: #1c1c1c;
    --rule: #2a2a2a;
    --accent-green: #6e9d2c;
    --accent-orange: #e8641e;
    --glow: #ffffff;
  }
  * { margin: 0; padding: 0; box-sizing: border-box; }
  html, body { width: 927px; height: 1200px; overflow: hidden; }
  body {
    position: relative;
    background: radial-gradient(ellipse 75% 60% at 50% 35%, var(--paper-light) 0%, var(--paper-mid) 60%, var(--paper-dark) 100%);
    color: var(--ink);
    font-family: "Tinos", "Times New Roman", serif;
  }
  .lamp-backdrop {
    position: absolute;
    left: 150px; top: 720px; width: 640px; height: 480px;
    background: radial-gradient(ellipse 50% 52% at 50% 55%, var(--glow) 0%, #f6f6f6 50%, rgba(225,225,225,0) 100%);
  }
  .flyer-title {
    position: absolute; top: 110px; left: 0; width: 927px;
    text-align: center;
    font-family: "Open Sans", Arial, sans-serif;
    font-weight: 600; font-size: 24.5px; line-height: 32px; letter-spacing: -0.2px;
  }
  .column { position: absolute; top: 150px; white-space: nowrap; }
  .column--left { left: 55px; width: 415px; }
  .column--right { left: 475px; width: 420px; }
  .tip-heading {
    font-family: "Open Sans", Arial, sans-serif;
    font-style: italic; font-weight: 700;
    font-size: 19px; line-height: 24px;
    margin: 12px 0 8px 3px;
  }
  .tip-heading--first { margin-top: 0; margin-bottom: 7px; }
  .tip-heading .green { color: var(--accent-green); }
  .tip-text { font-size: 18px; line-height: 22px; }
  .table-title {
    position: absolute; top: 782px; left: 63px;
    font-family: "Open Sans", Arial, sans-serif;
    font-weight: 600; font-size: 18.8px; line-height: 26px;
  }
  .light-calculator {
    position: absolute; top: 812px; left: 55px; width: 817px;
    border-collapse: collapse; table-layout: fixed;
    font-size: 18px; line-height: 21px;
  }
  .light-calculator td {
    border: 1.5px solid var(--rule);
    text-align: center; vertical-align: top;
    padding: 2px 2px 0;
    white-space: nowrap;
  }
  .light-calculator .row-size td { height: 46px; }
  .light-calculator .row-purpose td { height: 70px; }
  .light-calculator .row-purpose td.middle { vertical-align: middle; }
  .light-calculator .row-level td { height: 46.5px; }
  .light-calculator .row-note td { height: 25px; padding-top: 1px; }
  .site-name {
    position: absolute; top: 1093px; right: 55px;
    font-family: "Open Sans", Arial, sans-serif;
    font-size: 17px; line-height: 22px; color: var(--accent-orange);
  }
</style>
</head>
<body>
  <div class="lamp-backdrop" role="img" aria-label="Photo of a white globe floor lamp glowing softly behind the table"></div>

  <h1 class="flyer-title">Your guide to the perfect interior lighting</h1>

  <section class="column column--left">
    <p class="tip-text">The best light there is, is natural light. However with<br>the winter in-sight and daytime light shrinking, we<br>more and more depend on artificial lights to light up<br>our living spaces and make our homes sparkle in the<br>dark, feel warmer, cozier and safer.&nbsp; If you’re contem-<br>plating new light fixtures for your house, here are few<br>hints to help you choose the right luminaire:</p>

    <h2 class="tip-heading">Determine what your lighting goals are.</h2>
    <p class="tip-text">Direct or task lighting is focused in the space you are<br>trying to work. Ambient or indirect lighting is used<br>for ambiance and for overall lighting of a space. Once<br>chosen you can begin to choose lighting options.<br>Each room in your home should have a mood you<br>want to set, as well as a function you want your light-<br>ing to serve. Choose the right amount of light for your<br>room by using the calculation under.</p>

    <h2 class="tip-heading">Use multiple light sources for one space.</h2>
    <p class="tip-text">This will help you to achieve a variety of functions<br>and activities in one space and it will reduce shad-<br>ows.&nbsp; Have a mix of light sources at different levels<br>(recessed, suspension lamps, wall scones,…) to create<br>a flattering ambience and add appropriate task light-<br>ing for whatever you do in that space. In the kitchen,<br>under counter lights can provide great task lighting.<br>While in a living room, opt for a floor lamp next to a<br>couch or favorite reading chair</p>
  </section>

  <section class="column column--right">
    <h2 class="tip-heading tip-heading--first">Choose your chandeliers wisely.</h2>
    <p class="tip-text">Because of the central position in a space a chande-<br>lier determines largely the decorating value of it. Ask<br>yourself if you want it to be an eye catcher or should<br>it blend in?&nbsp; In any way and whichever is your décor<br>choice, measure out the space, and ceiling height<br>before ordering to ensure enough head room will be<br>available below the hanging chandelier.</p>

    <h2 class="tip-heading">Highlight the room’s highlights.</h2>
    <p class="tip-text">Dramatize wall textures, accent artwork or light up<br>the fireplace. Draw the attention within the space to<br>the architecture and decorative highlights of it. You<br>can do this with special adjustable spot lighting that is<br>either recessed or on a track or use upwards lighting<br>wall scones.</p>

    <h2 class="tip-heading">Go for <span class="green">green</span> and save!</h2>
    <p class="tip-text">85% of the cost of lighting are energy costs so it pays<br>off rather fast to switch to energy saving alternatives<br>like LED. A little bit more expensive at the registry<br>but far cheaper on your next energy bill. Don’t like<br>the white color? Look on the packaging for the color<br>temperature; 2700K is perfect for ambiance, 3000k for<br>task lighting.</p>
  </section>

  <h2 class="table-title">Calculate yourself how much light you really need</h2>
  <table class="light-calculator">
    <colgroup>
      <col style="width:180px"><col style="width:122px"><col style="width:43px"><col style="width:116px"><col style="width:124px"><col style="width:78px"><col style="width:154px">
    </colgroup>
    <tr class="row-size">
      <td>How big is the area?</td><td>Width (A)</td><td></td><td>Length(B)</td><td></td><td>Surface<br>(A)x(B)</td><td>(C)</td>
    </tr>
    <tr class="row-purpose">
      <td>What is the purpose of<br>the area?</td>
      <td colspan="2" style="padding-top:23px">LED or CFLI light-<br>ing</td>
      <td>Total Lumen<br>needed<br>(C) x (D)</td>
      <td colspan="2" class="middle">Incandescent lighting</td>
      <td>Total Watt needed<br>(C) x (E)</td>
    </tr>
    <tr class="row-level">
      <td>Relax, Watch Tv, Talk</td><td>Lumen per Sq<br>ft (D)</td><td>20</td><td></td><td>Watt per Sq ft<br>(E)</td><td>1.5</td><td></td>
    </tr>
    <tr class="row-level">
      <td>Have dinner, dress up</td><td>Lumen per Sq<br>ft (D)</td><td>30</td><td></td><td>Watt per Sq ft<br>(E)</td><td>2</td><td></td>
    </tr>
    <tr class="row-level">
      <td>Cook, Work, Read</td><td>Lumen per Sq<br>ft (D)</td><td>50</td><td></td><td>Watt per Sq ft<br>(E)</td><td>3.5</td><td></td>
    </tr>
    <tr class="row-note">
      <td colspan="7">Simple add up the wattage or Lumen of the light bulbs in the space to see if you meet the total light needed</td>
    </tr>
  </table>

  <p class="site-name">brenovaka.example</p>
</body>
</html>
```